make it look old timey and motherly but mordern...bath soak with cooling vapors. hazel hearth co

need a bath soak label...cooling vapors. will be in a pouch like below. dont pay attention to the design, just attatching so you know the kind of pouch itll be in. need something trusty, minimal and clean...its called hazel hearth co bath soak the best bath yull ever take.... for sore muscles, cooling vapors, smells good...made with menthol lemon and eucalyptus...give me something good.

Target Market(s)

make it look old timey and motherly but mordern

Font styles to use
Serif
Sans Serif

Colors
0054AA
0677BA
7BADD7
CADEEF
E8F1F8
0094D4
00A9DD
6FCCEA
C7EBF8
E9F6FB
FFF300
FFF600
FEFA6F
FFFEC7
FFFEE8
FFC000
F8CF3A
FAE287
FDF2CF
FEFAEE
E54698
E96AAD
F1A4CE
F9D9EA
FCEFF6
6B429C
8869AF
B7A5CE
E3DAEB
F3F0F8

```html
<!DOCTYPE html>
<html lang="en">
<head>
<meta charset="utf-8">
<title>hazel hearth co — Bath Soak</title>
<link rel="stylesheet" href="https://fonts.googleapis.com/css2?family=Montserrat:wght@300;500;600;700&display=swap">
<style>
  :root {
    --teal-deep: #1d8a9c;
    --teal: #3aa6bb;
    --teal-light: #86c8d8;
    --mist: #c9b3b9;
    --coral: #e38f8f;
    --coral-deep: #d46e6a;
    --paper: #f3f3f3;
    --ink-light: #f4f4f4;
  }
  * { box-sizing: border-box; margin: 0; padding: 0; }
  html, body {
    width: 986px;
    height: 1200px;
    overflow: hidden;
    background: #ffffff;
  }
  .label {
    position: relative;
    width: 986px;
    height: 1200px;
    overflow: hidden;
    font-family: "Montserrat", sans-serif;
    color: var(--ink-light);
    background:
      linear-gradient(to bottom, var(--paper) 0%, rgba(243,243,243,0.92) 16%, rgba(243,243,243,0) 36%),
      linear-gradient(205deg, var(--teal) 0%, var(--teal-light) 30%, var(--mist) 55%, var(--coral) 78%, var(--coral-deep) 100%);
  }
  .top-band {
    position: absolute;
    left: 0;
    top: 0;
    width: 986px;
    height: 110px;
  }
  .brand-seal {
    position: absolute;
    left: 270px;
    top: 410px;
    width: 440px;
    height: 440px;
    border: 3px solid var(--ink-light);
    border-radius: 50%;
    display: flex;
    align-items: center;
    justify-content: center;
  }
  .brand-name {
    font-weight: 500;
    font-size: 66px;
    line-height: 1.1;
    text-align: center;
    color: var(--ink-light);
  }
  .product-type {
    position: absolute;
    left: 0;
    width: 100%;
    top: 876px;
    text-align: center;
    font-weight: 700;
    font-size: 20px;
    letter-spacing: 3px;
  }
  .tagline {
    position: absolute;
    left: 0;
    width: 100%;
    top: 904px;
    text-align: center;
    font-weight: 300;
    font-size: 19px;
    letter-spacing: 5px;
  }
  .scents {
    position: absolute;
    left: 0;
    width: 100%;
    top: 990px;
    display: flex;
    justify-content: center;
    gap: 44px;
  }
  .scent {
    width: 80px;
    display: flex;
    flex-direction: column;
    align-items: center;
    gap: 14px;
  }
  .scent-art {
    width: 64px;
    height: 64px;
    border-radius: 50%;
    background: rgba(244,244,244,0.22);
  }
  .scent-name {
    font-weight: 600;
    font-size: 13px;
    letter-spacing: 1px;
  }
  .base-stripe {
    position: absolute;
    left: 0;
    width: 100%;
    top: 1096px;
    height: 18px;
    background: var(--teal-deep);
  }
  .weight-band {
    position: absolute;
    left: 0;
    width: 100%;
    top: 1126px;
    height: 42px;
    background: var(--teal-deep);
    display: flex;
    align-items: center;
    justify-content: center;
    font-weight: 700;
    font-size: 17px;
    letter-spacing: 1px;
  }
</style>
</head>
<body>
  <main class="label">
    <svg class="top-band" viewBox="0 0 986 110" aria-hidden="true">
      <path d="M0 0 H986 V36 C760 40 560 60 483 96 C410 60 220 40 0 36 Z" fill="var(--teal-deep)"/>
    </svg>

    <div class="brand-seal">
      <p class="brand-name">hazel<br>hearth<br>co</p>
    </div>

    <h1 class="product-type">BATH SOAK</h1>
    <p class="tagline">the best bath you’ll ever take</p>

    <ul class="scents" style="list-style:none">
      <li class="scent">
        <div class="scent-art" role="img" aria-label="Line drawing of a mint leaf"></div>
        <span class="scent-name">menthol</span>
      </li>
      <li class="scent">
        <div class="scent-art" role="img" aria-label="Line drawing of a lemon half"></div>
        <span class="scent-name">lemon</span>
      </li>
      <li class="scent">
        <div class="scent-art" role="img" aria-label="Line drawing of a eucalyptus sprig"></div>
        <span class="scent-name">eucalyptus</span>
      </li>
    </ul>

    <div class="base-stripe"></div>
    <div class="weight-band">425 gram</div>
  </main>
</body>
</html>
```